Typing Service Business Card Design

Need a new business card design for new logo update. The Keyline Crew is an outsourced typing service. We type audio / voice files into word documents. We are a professional service that is recognised in the industry over the past 15 years and have a strong connection to our brand. The final design should be professional, simple, yet effective.

Business

Contact Information for Business Card

Rosalind Varga
Director

rosalind@kbq.com.au
www.thekeylinecrewbase.com.au

```html
<!DOCTYPE html>
<html lang="en">
<head>
<meta charset="utf-8">
<title>The Keyline Crew – Business Card</title>
<link rel="stylesheet" href="https://fonts.googleapis.com/css2?family=Roboto+Condensed:wght@300;400;700&display=swap">
<style>
  :root {
    --pink: #d65db6;
    --ink: #141214;
    --paper: #ffffff;
    --stage: #e9e6e2;
    --muted: #1d1b1d;
  }
  * { box-sizing: border-box; margin: 0; padding: 0; }
  html, body {
    width: 1200px; height: 892px; overflow: hidden;
    background: var(--stage);
    font-family: "Roboto Condensed", Arial, sans-serif;
  }
  .canvas {
    width: 1200px; height: 892px;
    display: flex; flex-direction: column; align-items: center; justify-content: center;
    gap: 40px;
  }
  .card {
    position: relative;
    width: 660px; height: 377px;
    overflow: hidden;
    box-shadow: 0 4px 14px rgba(0,0,0,.18);
  }

  /* Front */
  .card--front { background: var(--paper); color: var(--ink); }
  .brand-name {
    position: absolute; right: 40px; top: 58px;
    font-weight: 700; font-size: 40px; color: var(--pink);
    display: flex; align-items: center; gap: 12px;
    letter-spacing: -0.5px;
  }
  .brand-dot { width: 14px; height: 14px; background: var(--pink); border-radius: 50%; }
  .rule { position: absolute; left: 0; right: 0; height: 3px; background: var(--pink); }
  .rule--top { top: 138px; }
  .rule--bottom { top: 216px; }
  .band {
    position: absolute; left: 0; right: 0; top: 148px; height: 58px;
    background: var(--ink);
    display: flex; align-items: center; justify-content: space-between;
    padding: 0 34px;
  }
  .person-name { color: var(--pink); font-size: 36px; font-weight: 400; }
  .band-tagline { color: var(--paper); font-size: 32px; font-weight: 300; }
  .role {
    position: absolute; left: 34px; top: 228px;
    font-size: 24px; font-weight: 400; color: var(--muted);
  }
  .contacts {
    position: absolute; right: 34px; bottom: 32px;
    list-style: none; display: flex; flex-direction: column; gap: 10px; align-items: flex-end;
  }
  .contact { display: flex; align-items: center; gap: 12px; font-size: 21px; color: var(--muted); }
  .contact-icon { width: 22px; height: 22px; display: block; }

  /* Back */
  .card--back {
    background: var(--ink);
    display: flex; flex-direction: column; justify-content: center; padding-left: 90px;
  }
  .back-brand {
    font-weight: 700; font-size: 62px; color: var(--pink);
    letter-spacing: -1px;
  }
  .back-tagline {
    margin-top: 26px; margin-left: 150px;
    font-weight: 300; font-size: 44px; color: var(--paper);
  }
</style>
</head>
<body>
<main class="canvas">
  <section class="card card--front" aria-label="Business card front">
    <div class="brand-name"><span class="brand-dot"></span>The Keyline Crew</div>
    <div class="rule rule--top"></div>
    <div class="band">
      <span class="person-name">Rosalind Varga</span>
      <span class="band-tagline">You speak. We key.</span>
    </div>
    <div class="rule rule--bottom"></div>
    <p class="role">Director</p>
    <ul class="contacts">
      <li class="contact">rosalind@kbq.com.au
        <svg class="contact-icon" viewBox="0 0 22 22" aria-hidden="true">
          <rect width="22" height="22" fill="#d65db6"/>
          <rect x="4" y="6" width="14" height="10" fill="none" stroke="#fff" stroke-width="1.5"/>
          <path d="M4 6 L11 12 L18 6" fill="none" stroke="#fff" stroke-width="1.5"/>
        </svg>
      </li>
      <li class="contact">www.thekeylinecrewbase.com.au
        <svg class="contact-icon" viewBox="0 0 22 22" aria-hidden="true">
          <rect width="22" height="22" fill="#d65db6"/>
          <circle cx="11" cy="11" r="6.5" fill="none" stroke="#fff" stroke-width="1.5"/>
          <ellipse cx="11" cy="11" rx="2.8" ry="6.5" fill="none" stroke="#fff" stroke-width="1.2"/>
          <path d="M4.5 11 H17.5" stroke="#fff" stroke-width="1.2"/>
        </svg>
      </li>
    </ul>
  </section>

  <section class="card card--back" aria-label="Business card back">
    <p class="back-brand">The Keyline Crew</p>
    <p class="back-tagline">You speak. We key.</p>
  </section>
</main>
</body>
</html>
```